Foldable creative restaurant menu

We require foldable restaurant menu to be placed on the each table, want it to look creative and modern with pages representing pictures of the dish not all dishes but few to represent what we do.Please get creative make sure its different, the colour should represent classy restaurant, not cheap and fast. The shape of the menu can be difference creative words must be easy to read and the logo must be in the menu here and there briefly.

Target Market(s)

Restaurant customers

Industry/Entity Type

Health And Wellness

Colors

Designer to choose colors to be used in the design.

Requirements
Must have
• foldable, must have good dish presentation pictures and must look modern and classy
Nice to have
• funky design and creative can be not just square foldable but can be interesting shape of menu.
Should not have
• boring plain spaces
• small writing
• dark pictures

```html
<!DOCTYPE html>
<html lang="en">
<head>
<meta charset="utf-8">
<title>Restaurant Menu – Trifold Inside</title>
<link href="https://fonts.googleapis.com/css2?family=Oswald:wght@500;600&family=Questrial&display=swap" rel="stylesheet">
<style>
  :root {
    --leaf: #8cc63f;
    --leaf-dot: #7cbb2f;
    --ink: #1f1f1f;
    --body: #5e5e5e;
    --card: rgba(255,255,255,0.93);
    --rule: #2a2a2a;
  }
  * { margin: 0; padding: 0; box-sizing: border-box; }
  html, body { width: 1200px; height: 849px; overflow: hidden; background: #fff; }
  .menu { position: relative; width: 1200px; height: 849px; overflow: hidden; font-family: "Questrial", sans-serif; }
  .panel-photo { position: absolute; top: 0; width: 400px; height: 849px; }
  .photo-salad { left: 0; background: radial-gradient(ellipse at 30% 45%, #6f9b3a 0%, #3f6e27 35%, #c99a4a 60%, #e8e6df 100%); }
  .photo-main { left: 400px; background: linear-gradient(180deg, #dcdcdc 0%, #4f7a2c 10%, #3a6a22 22%, #9a3b25 45%, #b24a2e 62%, #e9e5dc 85%, #f2f2f2 100%); }
  .photo-parmi { left: 800px; background: radial-gradient(ellipse at 40% 40%, #f6efd8 0%, #e8d6a0 35%, #c98a3a 60%, #e9dcc0 80%, #f1efe8 100%); }
  .folds { position: absolute; inset: 0; }
  .card { position: absolute; top: 86px; height: 708px; background: var(--card); padding: 18px 22px 0; }
  .card-salad { left: 64px; width: 272px; border: 2px dotted var(--leaf-dot); }
  .card-main { left: 464px; width: 271px; }
  .card-more { left: 882px; width: 272px; }
  .section-title { font-family: "Oswald", sans-serif; font-weight: 600; color: var(--leaf); font-size: 25px; line-height: 26px; letter-spacing: -0.8px; text-transform: uppercase; transform: scale(0.88, 1.2); transform-origin: left top; margin-bottom: 18px; white-space: nowrap; }
  .section-title .price { font-family: "Questrial", sans-serif; font-size: 11px; color: var(--ink); margin-left: 6px; letter-spacing: 0; }
  .dish { margin-bottom: 11px; }
  .dish-name { font-size: 10.8px; color: var(--ink); text-transform: uppercase; line-height: 14.3px; letter-spacing: -0.1px; }
  .dish-name .price { margin-left: 7px; }
  .dish-desc { font-size: 10.3px; color: var(--body); line-height: 14.3px; letter-spacing: -0.15px; }
  .dish-desc .extra { color: var(--ink); }
  .add-on { font-size: 10.8px; color: var(--ink); line-height: 14.3px; margin-bottom: 11px; text-transform: uppercase; letter-spacing: -0.1px; }
  .gap-soup { margin-top: 44px; }
  .gap-pasta { margin-top: 50px; }
  .sides { font-size: 10.8px; color: var(--ink); margin-bottom: 16px; }
  .sides span { margin-right: 12px; }
  .kids .dish { margin-bottom: 9.5px; }
  .card-more .section-title { margin-bottom: 16px; }
</style>
</head>
<body>
<div class="menu">
  <div class="panel-photo photo-salad" role="img" aria-label="Photo of a fresh green salad with spinach, cheese and crispy toppings"></div>
  <div class="panel-photo photo-main" role="img" aria-label="Photo of grilled steak with broccoli and steamed rice"></div>
  <div class="panel-photo photo-parmi" role="img" aria-label="Photo of chicken parmigiana with melted mozzarella and chips"></div>

  <svg class="folds" width="1200" height="849" viewBox="0 0 1200 849" aria-hidden="true">
    <g stroke="var(--rule)" stroke-width="0.8" fill="none">
      <path d="M28 0 L0 105 M368 0 L400 105 L432 0 M768 0 L800 105 L832 0 M1168 0 L1200 105"/>
      <path d="M0 742 L34 849 M400 742 L366 849 M400 742 L434 849 M800 742 L766 849 M800 742 L834 849 M1200 742 L1166 849"/>
    </g>
  </svg>

  <section class="card card-salad">
    <h2 class="section-title">Salad</h2>
    <div class="dish"><p class="dish-name">Asian Chicken Fusion Salad<span class="price">15</span></p>
      <p class="dish-desc">Grilled chicken served with a medley of fresh salad greens, sesame nut crumb and a light sweet chilli, sesame and soy dressing</p></div>
    <div class="dish"><p class="dish-name">Caesar Salad<span class="price">15</span></p>
      <p class="dish-desc">Baby Cos lettuce, crispy bacon, garlic croutons, flaked parmesan cheese, boiled egg in Caesar dressing</p></div>
    <p class="add-on">Add Chicken $4.00<br>Smoked Salmon $5.00</p>
    <div class="dish"><p class="dish-name">House Salad<span class="price">10</span></p>
      <p class="dish-desc">Crispy lettuce mix, tomato, cucumber, spinach, red onion, Kalamata olives and feta cheese drizzled with house dressing</p></div>
    <p class="add-on">Add Chicken $4<br>Smoked Salmon $5</p>

    <h2 class="section-title gap-soup">Soup of the Day<span class="price">8</span></h2>

    <h2 class="section-title gap-pasta">Pasta</h2>
    <div class="dish"><p class="dish-name">Fettuccine Carbonara<span class="price">15</span></p>
      <p class="dish-desc">Fettuccine served with pan seared sliced ham, bacon, shallots and onion in a creamy garlic sauce</p></div>
    <div class="dish"><p class="dish-name">Fettuccine Matriciana - V<span class="price">15</span></p>
      <p class="dish-desc">Fettuccine served with sun dried tomatoes, capsicum, zucchini, mushroom, onion, shallot and garlic in a Napoli sauce</p></div>
    <div class="dish"><p class="dish-name">Spaghetti Bolognese<span class="price">15</span></p>
      <p class="dish-desc">Spaghetti cooked al dente and pan tossed with a traditional Italian style meat sauce</p></div>
  </section>

  <section class="card card-main">
    <h2 class="section-title">Main</h2>
    <div class="dish"><p class="dish-name">Salmon Skin On<span class="price">25</span></p>
      <p class="dish-desc">Salmon fillet on the skin, grilled - THE WAY YOU LIKE IT<br>Served with choices of the following:<br>garden salad - steamed vegetables - rice<br><span class="extra">ADD Sauce - hollandaise, lemon butter</span></p></div>
    <div class="dish"><p class="dish-name">Steak of the Day<span class="price">25</span></p>
      <p class="dish-desc">Steak of the day cooked<br>(rare, medium or well done)<br>Served with TWO choices of the following:<br>Chips - Garden salad - steamed vegetables<br><span class="extra">ADD Sauce - Pepper, Mushroom OR Garlic</span></p></div>
    <div class="dish"><p class="dish-name">Barramundi Fillet<span class="price">23</span></p>
      <p class="dish-desc">Barramundi fillet served on the bed of rice with creamy white wine sauce<br>Served with TWO choices of the following:<br>Chips - Garden salad - steamed vegetables<br><span class="extra">ADD Sauce - tartare, lemon butter</span></p></div>
    <div class="dish"><p class="dish-name">Lamb Shank<span class="price">25</span></p>
      <p class="dish-desc">Slow cooked lamb shank served with mashed potato and vegetables (zucchini, carrot, broccoli) in tomato red wine mixed herb sauce</p></div>
    <div class="dish"><p class="dish-name">Roast of the Day <span style="text-transform:none">(beef or pork)</span><span class="price">25</span></p>
      <p class="dish-desc">Roasted pork or beef served with mashed potato and vegetables (zucchini, carrot, broccoli) with gravy sauce (cooked with onion, celery, carrot, herb mix and red wine)</p></div>
    <div class="dish"><p class="dish-name">Mushroom Risotto<span class="price">20</span></p>
      <p class="dish-desc">Vegetarian mushroom risotto with Arborio rice</p></div>
    <div class="dish"><p class="dish-name">Pork Scallopini<span class="price">23</span></p>
      <p class="dish-desc">Medallions of pork fried in a mushroom white wine sauce with a steamed vegetables and mashed potato</p></div>
    <div class="dish"><p class="dish-name">Italian Style Breast Fillet<br><span style="text-transform:none">with pesto sauce 23</span></p>
      <p class="dish-desc">Grilled chicken breast fillet with steamed vegetables and pesto cream sauce</p></div>
  </section>

  <section class="card card-more">
    <div class="dish"><p class="dish-name">Chicken Parmigiana<span class="price">17</span></p>
      <p class="dish-desc">Lightly crumbed oven baked chicken breast topped with Napoli sauce, ham and mozzarella served with chips and garden salad</p></div>
    <div class="dish"><p class="dish-name">Chicken Carbonara Parmigiana<span class="price">17</span></p>
      <p class="dish-desc">Lightly crumbed oven baked chicken breast topped with bacon, garlic, cream sauce and mozzarella served with chip and garden salad</p></div>
    <div class="dish"><p class="dish-name">Classic Beef Burger<span class="price">15</span></p>
      <p class="dish-desc">Beef patty served with cheese, bacon, lettuce and tomato with Chips on the side<br>Choice of sauce - Tomato, BBQ or Tomato Relish</p></div>
    <div class="dish"><p class="dish-name">Club Sandwich<span class="price">20</span></p>
      <p class="dish-desc">Big 3 layers sandwich with chicken, bacon, eggs, tomato and lettuce, served with chips</p></div>
    <div class="dish"><p class="dish-name">Nachos<span class="price">16</span></p>
      <p class="dish-desc">Corn chips, beef, salsa, tasty cheese, grilled to perfection</p></div>
    <div class="dish"><p class="dish-name">Salt and Pepper Squid<span class="price">15</span></p>
      <p class="dish-desc">Squid, wedges with light sour cream and sweet chilli sauce</p></div>
    <div class="dish"><p class="dish-name">Fish and Chips<span class="price">12</span></p>
      <p class="dish-desc">Fish, chips, salad and tartar sauce</p></div>

    <h2 class="section-title">Sides</h2>
    <p class="sides"><span>CHIPS 4</span><span>GARDEN SALAD 6</span><span>RICE 3</span></p>

    <h2 class="section-title">Kid's Meal</h2>
    <div class="kids">
      <div class="dish"><p class="dish-name">Cardinale Pizza &amp; Chips<span class="price">10</span></p>
        <p class="dish-desc">Mozzarella cheese and Ham served with chips</p></div>
      <div class="dish"><p class="dish-name">Spaghetti Bolognese<span class="price">7</span></p></div>
      <div class="dish"><p class="dish-name">Spaghetti with Meatballs<span class="price">7</span></p></div>
      <div class="dish"><p class="dish-name">Cheeseburger and Chips<span class="price">7</span></p></div>
      <div class="dish"><p class="dish-name">Fish and Chips<span class="price">7</span></p></div>
      <div class="dish"><p class="dish-name">Chips and Nuggets<span class="price">7</span></p></div>
    </div>
  </section>
</div>
</body>
</html>
```